Design Business Cards

TK construction is a construction company. business card should have:
- License #
- position
- name
- cell #
- office #
- website
any other ideas are welcome!

```html
<!DOCTYPE html>
<html lang="en">
<head>
<meta charset="utf-8">
<title>TK construction – Business Cards</title>
<link rel="stylesheet" href="https://fonts.googleapis.com/css2?family=Lato:wght@400;700&family=Montserrat:wght@700&display=swap">
<style>
  :root {
    --gold: #b8952c;
    --ink: #0e0e0e;
    --paper: #ffffff;
    --backdrop: #e8e5df;
    --text: #1b1b1b;
  }
  * { box-sizing: border-box; margin: 0; padding: 0; }
  html, body { width: 1200px; height: 900px; overflow: hidden; }
  body {
    background: var(--backdrop);
    font-family: "Lato", sans-serif;
    color: var(--text);
    position: relative;
  }
  .card {
    position: absolute;
    left: 230px;
    width: 740px;
    height: 420px;
    background: var(--paper);
    border-radius: 22px;
    overflow: hidden;
    box-shadow: 0 6px 20px rgba(0,0,0,0.15);
  }
  .card--back { top: 20px; }
  .card--front { top: 460px; }
  .card__shapes { position: absolute; inset: 0; width: 100%; height: 100%; }

  .brand {
    position: absolute;
    display: flex;
    align-items: center;
    gap: 12px;
    font-family: "Montserrat", sans-serif;
    font-weight: 700;
    color: var(--ink);
    letter-spacing: 0.5px;
  }
  .brand__mark { background: var(--gold); display: block; }

  .card--back .brand { top: 110px; left: 70px; right: 0; justify-content: center; font-size: 42px; }
  .card--back .brand__mark { width: 34px; height: 34px; }
  .back__website {
    position: absolute;
    top: 264px;
    left: 150px;
    font-size: 22px;
    color: var(--ink);
  }

  .card--front .brand { top: 42px; left: 46px; font-size: 24px; }
  .card--front .brand__mark { width: 22px; height: 22px; }
  .holder { position: absolute; top: 120px; left: 46px; }
  .holder__name { font-size: 32px; font-weight: 700; letter-spacing: -0.3px; }
  .holder__role { font-size: 15px; margin-top: 4px; }

  .licence {
    position: absolute;
    top: 132px;
    right: 112px;
    display: flex;
    align-items: center;
    gap: 14px;
    color: var(--gold);
    font-size: 28px;
  }
  .licence svg { width: 40px; height: 40px; }

  .contact {
    position: absolute;
    top: 214px;
    right: 180px;
    list-style: none;
    text-align: right;
    font-size: 17px;
    line-height: 32px;
  }
  .contact__icons {
    position: absolute;
    top: 222px;
    left: 633px;
    width: 44px;
  }
  .contact__icons svg { display: block; width: 22px; height: 22px; margin: 0 auto 10px; }
</style>
</head>
<body>

  <section class="card card--back" aria-label="Business card, back">
    <svg class="card__shapes" viewBox="0 0 740 420" aria-hidden="true">
      <rect x="0" y="0" width="70" height="420" fill="var(--ink)"/>
      <polygon points="0,245 470,245 490,270 470,295 0,295" fill="var(--gold)"/>
    </svg>
    <div class="brand"><span class="brand__mark"></span>TK construction</div>
    <p class="back__website">www.tkbuildgroup.com</p>
  </section>

  <section class="card card--front" aria-label="Business card, front">
    <svg class="card__shapes" viewBox="0 0 740 420" aria-hidden="true">
      <polygon points="690,0 740,0 740,420 600,420 600,385 690,350" fill="var(--ink)"/>
      <polygon points="0,370 60,420 0,420" fill="var(--ink)"/>
      <polygon points="620,210 690,210 690,350 620,378" fill="var(--gold)"/>
    </svg>

    <div class="brand"><span class="brand__mark"></span>TK construction</div>

    <div class="holder">
      <h1 class="holder__name">Daniel Morris</h1>
      <p class="holder__role">Ceo, Founder</p>
    </div>

    <div class="licence">
      <span>Licence no</span>
      <svg viewBox="0 0 40 40" aria-hidden="true">
        <rect x="3" y="4" width="30" height="26" fill="none" stroke="var(--ink)" stroke-width="2.5"/>
        <circle cx="24" cy="24" r="6" fill="var(--paper)" stroke="var(--ink)" stroke-width="2.5"/>
        <polyline points="21,29 21,37 24,35 27,37 27,29" fill="none" stroke="var(--ink)" stroke-width="2"/>
        <line x1="9" y1="12" x2="26" y2="12" stroke="var(--ink)" stroke-width="2"/>
      </svg>
    </div>

    <ul class="contact">
      <li>+8801755420981</li>
      <li>daniel@tkbuildgroup.org</li>
      <li>www.tkbuildgroup.com</li>
      <li>42/B,park road lalmatia,1207</li>
    </ul>

    <div class="contact__icons" aria-hidden="true">
      <svg viewBox="0 0 24 24"><path d="M6 3l4 4-2 3c1 2 3 4 5 5l3-2 4 4-3 3C10 20 4 14 3 6z" fill="var(--paper)"/></svg>
      <svg viewBox="0 0 24 24"><polygon points="2,11 22,3 16,21 12,14" fill="var(--paper)"/></svg>
      <svg viewBox="0 0 24 24"><g fill="none" stroke="var(--paper)" stroke-width="2"><circle cx="12" cy="12" r="9"/><ellipse cx="12" cy="12" rx="4" ry="9"/><line x1="3" y1="12" x2="21" y2="12"/></g></svg>
      <svg viewBox="0 0 24 24"><rect x="4" y="3" width="16" height="18" fill="var(--paper)"/><g fill="var(--gold)"><rect x="7" y="6" width="3" height="3"/><rect x="14" y="6" width="3" height="3"/><rect x="7" y="11" width="3" height="3"/><rect x="14" y="11" width="3" height="3"/><rect x="10" y="16" width="4" height="5"/></g></svg>
    </div>
  </section>

</body>
</html>
```